Landing Page Design for Velpora Casino (Contest)

We need a landingpage design for Velpora casino. (www.velpora-example.com) We would like to signal the same feeling as you experience when you visit the actual website. It is a bit cartoony. The final design should communicate a safe gaming environment. I attached a Wireframe to give you the feeling, of how we see the different components included on this landingpage. The wireframe is meant as inspiration, if you want to freestyle it a bit, give it a go !

```html
<!DOCTYPE html>
<html lang="en">
<head>
<meta charset="utf-8">
<title>Velpora Casino – Landing Page</title>
<link href="https://fonts.googleapis.com/css2?family=Lobster&family=Questrial&display=swap" rel="stylesheet">
<style>
:root{
  --ink:#222;
  --hero-dark:#2a2a2a;
  --mint-bg:#eef5f2;
  --teal:#22ad9c;
  --green:#1fa34a;
  --orange:#f47c3c;
  --cream:#fdf0d4;
  --mint:#bfe8d6;
  --space:#1d2a3a;
  --space-glow:#2e6f78;
  --purple:#8b4f8f;
  --chip:#c9321f;
  --line:#dfe7e3;
  --icon-bg:#f6e6dc;
  --white:#fff;
}
*{box-sizing:border-box;margin:0;padding:0}
html,body{width:1200px;height:3303px;overflow:hidden}
body{font-family:"Questrial",Arial,sans-serif;color:var(--ink);background:var(--white);position:relative}
.script{font-family:"Lobster",cursive;font-weight:400}
section,header,footer{position:absolute;left:0;width:1200px}
.abs{position:absolute}
.center{text-align:center}

/* hero */
.hero{top:0;height:495px;background:radial-gradient(circle at 50% 40%,#3a3a3a,var(--hero-dark) 70%)}
.topbar{top:0;height:50px;display:flex;align-items:center;padding:0 160px;justify-content:space-between;color:var(--white);font-size:12px;z-index:3}
.brand{font-family:"Lobster",cursive;font-size:24px;color:var(--white)}
.contacts{display:flex;gap:28px;align-items:center}
.contacts span{display:flex;align-items:center;gap:10px}
.contacts .sep{width:1px;height:22px;background:#888}
.hero-title{top:170px;width:1200px;color:var(--white);font-size:37px;line-height:54px}

.mint-zone{top:495px;height:723px;background:var(--mint-bg)}
.drip{left:44px;top:418px;width:92px;height:150px;background:var(--purple);border-radius:20px 20px 46px 46px;z-index:2}
.bonus{left:187px;top:355px;width:826px;height:299px;background:var(--white);box-shadow:0 4px 18px rgba(0,0,0,.15);display:flex;z-index:2}
.bonus-text{width:414px;display:flex;flex-direction:column;align-items:center;justify-content:center;text-align:center}
.bonus-text h2{font-size:31px;line-height:50px}
.btn-claim{margin-top:26px;background:var(--green);color:var(--white);font-size:13px;border-radius:22px;padding:13px 58px}
.bonus-photo{flex:1;background:linear-gradient(135deg,#3b3f44,#1b6b4a 75%,#0f4d33)}

.races-title{width:1200px;font-size:39px}
.races-sub{width:1200px;font-size:12px;color:var(--teal)}
.race{width:280px;text-align:center;font-size:12px;line-height:17px}
.race-icon{width:180px;height:180px;margin:0 auto;border-radius:50%;background:var(--icon-bg)}
.race p{margin:22px auto 0;width:225px}
.hl-orange{color:#f0a020}
.hl-green{color:var(--green)}
.btn-outline{border:1.5px solid var(--teal);color:var(--teal);border-radius:20px;font-size:12px;padding:8px 0;text-align:center;background:var(--white)}

/* winners */
.winners{top:1218px;height:627px;background:linear-gradient(160deg,var(--cream) 0%,var(--mint) 25%,var(--cream) 45%,var(--mint) 70%,var(--cream) 100%)}
.section-title{width:1200px;text-align:center;font-size:38px}
.story{top:143px;width:243px;height:401px;background:var(--white);border:1px solid #e7d9c2;border-radius:4px}
.story-photo{margin:15px 19px 0;height:165px;background:linear-gradient(135deg,#7a5b3c,#d9a46d 55%,#3c2a1c);box-shadow:0 3px 8px rgba(0,0,0,.3)}
.story h3{margin:30px 19px 0;color:var(--orange);font-size:16px;font-weight:700}
.story p{margin:14px 19px 0;font-size:11.5px;line-height:17px;color:#444}
.btn-small{position:absolute;left:16px;bottom:30px;width:116px;border:1.5px solid var(--orange);color:var(--orange);border-radius:18px;font-size:11px;padding:7px 0;text-align:center}

/* games */
.games{top:1845px;height:655px;background:radial-gradient(ellipse at 45% 55%,var(--space-glow) 0%,var(--space) 60%,#141b26 100%)}
.scallop{top:-12px;height:12px;width:1200px;background:radial-gradient(circle at 12px 12px,var(--space) 11px,transparent 12px) 0 0/24px 24px repeat-x}
.game{width:245px;height:165px;border:2px solid #111;box-shadow:0 3px 8px rgba(0,0,0,.5)}
.g1{background:linear-gradient(135deg,#101a2a,#2a6fd0 45%,#e03d6a 80%)}
.g2{background:linear-gradient(135deg,#c2223c,#e23a4f)}
.g3{background:linear-gradient(135deg,#3a2a5a,#a84080 55%,#f0c060)}
.g4{background:linear-gradient(135deg,#1a1a2a,#6a5a9a 50%,#d0b080)}
.g5{background:linear-gradient(135deg,#3a2020,#b02a30 55%,#2a1a1a)}
.chips{left:1035px;top:2411px;width:160px;height:166px;background:radial-gradient(circle at 60% 40%,#e0472f,var(--chip) 55%,transparent 70%);z-index:2}

/* reviews */
.reviews{top:2500px;height:528px;background:var(--mint-bg)}
.review-box{left:247px;top:134px;width:704px;height:152px;background:var(--white);border:1px solid var(--line);border-radius:8px;text-align:center;padding:24px 40px}
.review-box h4{color:var(--orange);font-size:13px;font-weight:700}
.review-box p{margin-top:10px;font-size:11.5px;line-height:19px;color:#444}
.arrow{width:36px;height:36px;border-radius:50%;background:var(--orange);display:flex;align-items:center;justify-content:center;top:191px}
.avatar{left:560px;top:246px;width:80px;height:80px;border-radius:50%;background:var(--white);border:1px solid var(--line);display:flex;align-items:center;justify-content:center}
.avatar span{width:48px;height:48px;border-radius:50%;background:linear-gradient(135deg,#f0c040,#3aa0d0)}
.divider{left:158px;top:378px;width:882px;height:2px;background:var(--line)}
.affiliate{top:418px;width:1200px;text-align:center;font-size:40px;color:#d2dcd8}

/* footer */
.site-footer{top:3028px;height:275px;background:var(--white)}
.foot-col{top:52px;list-style:none;font-size:12px;line-height:23.5px;color:#555}
.foot-brand{right:165px;top:88px;font-family:"Lobster",cursive;font-size:34px;color:var(--ink)}
.foot-line{left:158px;top:220px;width:882px;height:1px;background:var(--line)}
.pay{left:160px;top:239px;display:flex;gap:8px}
.pay span{width:40px;height:18px;border-radius:3px;background:#e4e8ee}
.social{left:887px;top:237px;display:flex;gap:9px}
.social span{width:26px;height:26px;border-radius:50%;border:1.5px solid #b8b8b8}
</style>
</head>
<body>

<section class="hero" aria-label="Hero">
  <header class="topbar abs">
    <div class="brand">Velpora</div>
    <div class="contacts">
      <span>
        <svg width="12" height="18" viewBox="0 0 12 18"><rect x="1" y="1" width="10" height="16" rx="2" fill="none" stroke="#fff" stroke-width="1.5"/><circle cx="6" cy="14" r="1" fill="#fff"/></svg>
        Call Us : 00 9876 5432
      </span>
      <i class="sep"></i>
      <span>
        <svg width="18" height="13" viewBox="0 0 18 13"><rect x="1" y="1" width="16" height="11" fill="none" stroke="#fff" stroke-width="1.5"/><path d="M1 1l8 6 8-6" fill="none" stroke="#fff" stroke-width="1.5"/></svg>
        Email : info@velpora-example.com
      </span>
    </div>
  </header>
  <h1 class="hero-title abs center script">This Guy Did Not Just Win 50€ Check<br>Out His Story Below</h1>
</section>

<section class="mint-zone" aria-label="Spin Sprints">
  <h2 class="races-title abs script center" style="top:213px">Try Spin Sprints</h2>
  <p class="races-sub abs center" style="top:281px">€1,000 cash + hundreds of prizes every day</p>

  <div class="race abs" style="left:124px;top:331px">
    <div class="race-icon" role="img" aria-label="Calendar icon surrounded by confetti"></div>
    <p>Spin Sprints are tournaments on Velpora that run every <span class="hl-orange">30 minutes 24/7.</span></p>
  </div>
  <div class="race abs" style="left:454px;top:331px">
    <div class="race-icon" role="img" aria-label="Slot machine icon surrounded by confetti"></div>
    <p>Use your Spin Sprint spins to collect as many <span class="hl-orange">wins, big wins, mega wins and wins in a row</span> before the clock runs out.</p>
  </div>
  <div class="race abs" style="left:785px;top:331px">
    <div class="race-icon" role="img" aria-label="Euro coin icon surrounded by confetti"></div>
    <p><span class="hl-green">Hundreds of prizes every day,</span> including €1,000 cash every evening at 20:00 CET.</p>
  </div>

  <div class="btn-outline abs" style="left:542px;top:622px;width:116px">Sign Up Now!</div>
</section>

<div class="drip abs" role="img" aria-label="Purple paint drip decoration"></div>
<div class="bonus abs">
  <div class="bonus-text">
    <h2 class="script">Welcome Bonus!<br>200 Free Sping &amp; Up To<br>1200€</h2>
    <span class="btn-claim">Claim Now!</span>
  </div>
  <div class="bonus-photo" role="img" aria-label="Poker player in a hoodie throwing two aces onto a green table"></div>
</div>

<section class="winners" aria-label="Winner Stories">
  <h2 class="section-title abs script" style="top:48px">Winner Stories!</h2>
  <article class="story abs" style="left:203px">
    <div class="story-photo" role="img" aria-label="Happy winner cheering in a casino"></div>
    <h3>Grand Jackpot</h3>
    <p>Lorem ipsum dolor sit amet, consectetur adipiscing elit, sed do eiusmod tempor incididunt ut labore et dolore magna aliqua. Ut enim ad minim</p>
    <span class="btn-small">Claim Now!</span>
  </article>
  <article class="story abs" style="left:478px">
    <div class="story-photo" role="img" aria-label="Players celebrating at a roulette table"></div>
    <h3>Magic Spinner</h3>
    <p>Lorem ipsum dolor sit amet, consectetur adipiscing elit, sed do eiusmod tempor incididunt ut labore et dolore magna aliqua. Ut enim ad minim</p>
    <span class="btn-small">Claim Now!</span>
  </article>
  <article class="story abs" style="left:753px">
    <div class="story-photo" role="img" aria-label="Man placing chips at a casino table"></div>
    <h3>Golden Temple</h3>
    <p>Lorem ipsum dolor sit amet, consectetur adipiscing elit, sed do eiusmod tempor incididunt ut labore et dolore magna aliqua. Ut enim ad minim</p>
    <span class="btn-small">Claim Now!</span>
  </article>
</section>

<section class="games" aria-label="Games">
  <div class="scallop abs"></div>
  <h2 class="section-title abs script" style="top:70px;color:var(--white)">Games</h2>
  <div class="game g1 abs" style="left:203px;top:155px" role="img" aria-label="Close-up of glowing slot machine reels"></div>
  <div class="game g2 abs" style="left:478px;top:155px" role="img" aria-label="Slot machine reels on a red background"></div>
  <div class="game g3 abs" style="left:755px;top:155px" role="img" aria-label="Woman playing slot machines"></div>
  <div class="btn-outline abs" style="left:542px;top:357px;width:116px;border-color:#fff;color:var(--ink)">Play Now!</div>
  <div class="game g4 abs" style="left:203px;top:423px" role="img" aria-label="Friends playing slot machines together"></div>
  <div class="game g5 abs" style="left:478px;top:423px" role="img" aria-label="Woman in red dress at a slot machine"></div>
  <div class="game g1 abs" style="left:755px;top:423px" role="img" aria-label="Close-up of glowing slot machine reels"></div>
</section>
<div class="chips abs" role="img" aria-label="Stack of red casino chips"></div>

<section class="reviews" aria-label="Customer Reviews">
  <h2 class="section-title abs script" style="top:58px">Customer Reviews</h2>
  <div class="review-box abs">
    <h4>Lorem Ipsum Dolor Sit Amet</h4>
    <p>Lorem ipsum dolor sit amet, consectetur adipiscing elit, sed do eiusmod tempor incididunt ut labore et dolore magna aliqua. Ut enim ad minim veniam, quis nostrud exercitation ullamco laboris nisi ut aliquip ex ea commodo consequat. Duis aute irure dolor in reprehenderit in voluptate velit esse cillum dolore eu</p>
  </div>
  <div class="arrow abs" style="left:229px"><svg width="10" height="12" viewBox="0 0 10 12"><path d="M7 1L2 6l5 5" fill="none" stroke="#fff" stroke-width="2"/></svg></div>
  <div class="arrow abs" style="left:933px"><svg width="10" height="12" viewBox="0 0 10 12"><path d="M3 1l5 5-5 5" fill="none" stroke="#fff" stroke-width="2"/></svg></div>
  <div class="avatar abs"><span role="img" aria-label="Reviewer avatar"></span></div>
  <div class="divider abs"></div>
  <div class="affiliate abs script">Affiliate</div>
</section>

<footer class="site-footer">
  <ul class="foot-col abs" style="left:160px">
    <li>Frontpage</li><li>About us</li><li>Fair Play Pledge</li><li>FAQ</li><li>Velpora games</li>
  </ul>
  <ul class="foot-col abs" style="left:330px">
    <li>Blog</li><li>Work at Velpora</li><li>Affiliates</li><li>Privacy Notice</li><li>Contact us</li>
  </ul>
  <ul class="foot-col abs" style="left:498px">
    <li>Terms &amp; Conditions</li>
  </ul>
  <div class="foot-brand abs">Velpora</div>
  <div class="foot-line abs"></div>
  <div class="pay abs" aria-label="Payment methods">
    <span></span><span></span><span></span><span></span><span></span><span></span><span></span><span></span>
  </div>
  <div class="social abs" aria-label="Social links">
    <span></span><span></span><span></span><span></span><span></span>
  </div>
</footer>

</body>
</html>
```